Sparrowgate Petals Website v.1 - attract floral shop franchisees

I need a simple information website for my new business. We are a franchisor of flower shops. The overall purpose of the website is to promote the company and the service, especially to potential franchisees and retailers. Only about 4 pages are required including homepage, About, For Supermarkets, For Franchisees, and Contact. No special functions are required except the site will have two separate inquiry forms that must be filled out online and submitted via automated email. Similarly, an email form should be linked from the Contact page. I have a logo and business cards designed by ArtQuarry, and I would like the site to have a consistent color scheme and style. The key to design will be to express the joy and love associated with flowers and floral bouquets.
IMPORTANT - I will be exporting the website design to Wordpress CMS in a site hosted by HostNimbus. For smooth integration into WordPress hosted by HostNimbus, the designer should build the site using a WordPress-friendly format. Ideally, they should use HTML, CSS, and PHP. Creating a custom theme or using a page builder that exports to WordPress-compatible files is best. This ensures the site can be easily imported and managed within WordPress.

Target Market(s)

Potential franchisees (existing florists or creative types who might like to own a floral business) and supermarkets who might want us to run their floral department

Industry/Entity Type

Floral retailing

Requirements
Must have
• A brand theme that is beautiful, consistent throughout and builds on the logo design
Nice to have
• Show gender and ethnic diversity in customers and florists. Pictures of happy florists (for franchisees) and pictures of amazing floral department displays (for supermarkets)

```html
<!DOCTYPE html>
<html lang="en">
<head>
<meta charset="utf-8">
<title>Sparrowgate Petals</title>
<link href="https://fonts.googleapis.com/css2?family=Bebas+Neue&family=Poppins:wght@400;500&display=swap" rel="stylesheet">
<style>
:root{
  --green:#0a8a3d;
  --orange:#f0a020;
  --ink:#111111;
  --text:#222222;
  --muted:#8a8a8a;
  --card:#f5f3ef;
  --line:#cfe6dc;
}
*{margin:0;padding:0;box-sizing:border-box}
html,body{width:1200px;height:675px;overflow:hidden;background:#fff}
body{position:relative;font-family:'Poppins',sans-serif;color:var(--text)}
.backdrop-curves{position:absolute;inset:0;z-index:0}
.abs{position:absolute;z-index:1}
.brand{left:100px;top:22px;display:flex;align-items:center;gap:8px}
.brand-dot{width:22px;height:22px;border-radius:50%;background:var(--orange)}
.brand-name{font-size:15px;font-weight:500;color:var(--orange)}
.main-nav{left:598px;top:26px;display:flex;gap:30px;font-size:15px;color:#222}
.nav-contact{left:1012px;top:22px;width:88px;height:30px;background:var(--green);color:#fff;font-size:15px;display:flex;align-items:center;justify-content:center;box-shadow:0 8px 18px rgba(0,0,0,.12)}
.hero-photo{left:100px;top:95px;width:320px;height:522px;background:linear-gradient(160deg,#8a7a5a 0%,#4f7a3a 35%,#6a6a68 60%,#e9b9b0 78%,#5e5a45 100%);box-shadow:0 10px 24px rgba(0,0,0,.12)}
.contact-row{left:460px;top:95px;display:flex;gap:20px;font-size:12px;color:var(--green);align-items:center}
.contact-row span{display:flex;align-items:center;gap:10px}
.headline{left:460px;top:130px;font-family:'Bebas Neue',sans-serif;font-size:60px;line-height:80px;color:var(--ink);white-space:nowrap}
.headline .o{color:var(--orange)}
.headline .g{color:var(--green)}
.intro{left:460px;top:299px;width:520px;font-size:15px;line-height:25px;color:var(--text)}
.btn-shop{left:460px;top:385px;width:150px;height:37px;background:var(--green);color:#fff;font-size:12px;display:flex;align-items:center;justify-content:center;box-shadow:0 10px 20px rgba(0,0,0,.12)}
.link-contact{left:640px;top:394px;font-size:12px;color:var(--green);display:flex;align-items:center;gap:12px}
.link-contact u{text-underline-offset:2px}
.stat{right:100px;text-align:right}
.stat-num{font-family:'Bebas Neue',sans-serif;font-size:32px;line-height:32px}
.stat-label{font-size:15px;color:#222;margin-top:6px}
.why-title{left:460px;top:472px;font-family:'Bebas Neue',sans-serif;font-size:26px;color:#222}
.feature{top:517px;width:203px;height:100px;background:var(--card);display:flex;align-items:center;padding:0 10px;gap:10px}
.feature-img{width:80px;height:80px;flex:none}
.feature h3{font-family:'Bebas Neue',sans-serif;font-weight:400;font-size:21px;color:#222;line-height:22px}
.feature p{font-size:11px;color:var(--muted);margin-top:6px}
</style>
</head>
<body>
<svg class="backdrop-curves" width="1200" height="675" viewBox="0 0 1200 675" fill="none" stroke="var(--line)" stroke-width="1">
  <path d="M0 170 C60 220 110 240 150 230"/>
  <path d="M0 290 C40 300 80 290 110 270"/>
  <path d="M0 500 C40 470 80 455 110 450"/>
  <path d="M270 0 C300 40 290 80 260 95"/>
  <path d="M500 0 C440 60 420 130 440 200"/>
  <path d="M620 60 C760 20 900 30 1000 80"/>
  <path d="M540 420 C580 520 620 610 650 675"/>
  <path d="M600 480 C700 560 760 640 790 675"/>
  <path d="M880 570 C960 560 1080 560 1200 540"/>
  <path d="M1080 675 C1120 620 1160 580 1200 560"/>
  <path d="M1130 0 C1160 20 1180 30 1200 40"/>
  <path d="M330 620 C340 640 345 660 340 675"/>
</svg>

<div class="abs brand"><span class="brand-dot"></span><span class="brand-name">Sparrowgate Petals</span></div>

<nav class="abs main-nav"><span>About Us</span><span>For Supermarkets</span><span>For Franchisees</span></nav>
<div class="abs nav-contact">Contact</div>

<div class="abs hero-photo" role="img" aria-label="Smiling florist arranging a bouquet of pink and white roses in a flower shop"></div>

<div class="abs contact-row">
  <span><svg width="14" height="14" viewBox="0 0 24 24" fill="none" stroke="currentColor" stroke-width="2"><path d="M22 16.9v3a2 2 0 0 1-2.2 2 19.8 19.8 0 0 1-8.6-3.1 19.5 19.5 0 0 1-6-6A19.8 19.8 0 0 1 2.1 4.2 2 2 0 0 1 4.1 2h3a2 2 0 0 1 2 1.7c.1 1 .4 1.9.7 2.8a2 2 0 0 1-.5 2.1L8 9.9a16 16 0 0 0 6 6l1.3-1.3a2 2 0 0 1 2.1-.5c.9.3 1.8.6 2.8.7a2 2 0 0 1 1.7 2z"/></svg>+44 20 7946 0182</span>
  <span><svg width="15" height="12" viewBox="0 0 24 18" fill="none" stroke="currentColor" stroke-width="2"><rect x="1" y="1" width="22" height="16"/><path d="M1 1l11 9 11-9M1 17l8-7M23 17l-8-7"/></svg>hello@sparrowgate.co</span>
</div>

<h1 class="abs headline">DISCOVER THE <span class="o">SPARROWGATE</span><br><span class="g">PETALS</span> DIFFERENCE.</h1>

<p class="abs intro">Enjoy top-quality flowers with professional service at affordable prices. Join our franchise network for exceptional support and growth opportunities.</p>

<div class="abs btn-shop">Shop Now</div>
<div class="abs link-contact"><u>Contact Us</u><svg width="16" height="10" viewBox="0 0 16 10" fill="none" stroke="currentColor" stroke-width="1.8"><path d="M0 5h14M10 1l4 4-4 4"/></svg></div>

<div class="abs stat" style="top:135px"><div class="stat-num" style="color:var(--green)">100+</div><div class="stat-label">Plants</div></div>
<div class="abs stat" style="top:246px"><div class="stat-num" style="color:var(--orange)">5000+</div><div class="stat-label">Customers</div></div>
<div class="abs stat" style="top:357px"><div class="stat-num" style="color:var(--green)">30+</div><div class="stat-label">Deliveries</div></div>

<h2 class="abs why-title">WHY CHOOSE US?</h2>

<div class="abs feature" style="left:460px">
  <div class="feature-img" role="img" aria-label="Colourful bunches of pink and yellow flowers" style="background:linear-gradient(135deg,#e45a7a,#f2c43a 60%,#d97a6a)"></div>
  <div><h3>QUALITY</h3><p>See more &gt;&gt;</p></div>
</div>
<div class="abs feature" style="left:678px">
  <div class="feature-img" role="img" aria-label="Flower market stall with buckets of blooms" style="background:linear-gradient(160deg,#b86a5a,#6f8a5a 50%,#2d3a3a)"></div>
  <div><h3>OPPORTUNITY</h3><p>See more &gt;&gt;</p></div>
</div>
<div class="abs feature" style="left:897px">
  <div class="feature-img" role="img" aria-label="Florist holding a fresh bouquet" style="background:linear-gradient(160deg,#5a7a3a,#707070 55%,#e6b4ab)"></div>
  <div><h3>SUPPORT</h3><p>See more &gt;&gt;</p></div>
</div>
</body>
</html>
```